Organic Herbs & Spices container

Greek startup company, which cultivate and trade spices and herbs (such as oregano, mint, thyme, sage etc.)

At present we are interested in only the type and shape of packaging which should be made by materials such as paper, cardboard, laminated paper and others based on paper or plastic.

Package size vary from 80g (2.82oz) - 300g (10.58oz). We are going to use the same packing for a variety of products with different information

* Please find attached our logo which should be included in the design.
* There is no company name available at the moment, however a name placeholder should be included.
* include a placeholder for the type of product (sage, oregano, mint, tea etc...).
* Each package should have a place in order to include product details and nutrition facts.

e.g.
xxxx (company name placeholder)
Sage (product type)
product details and nutrition facts.
Updates

Dear designers,first of all, thank you for your proposals. Please find bellow some updates for the project.- It is mandatory to include the logo into the design - Each package should be able to stored vertically - We are looking for one specific package design, please do not submit many variations of a certain package neither colour differentiations Thanks and good luck Added Wednesday, September 28, 2016

Please avoid the use of images. The same package will be used for all the kinds of products (only name and maybe colour will be different among different products. A transparent frame that will show the contents could be used too) Added Wednesday, September 28, 2016

Please find attached logo in EPS format

Our logo is the baseline, any concepts should be based on it. Try to avoid just adding the logo as a small sticker somewhere on the design. Please try to create around it at any way toy like. This could be, to visualize it as a 3D shape or object which can be used as the container of the products.

Reason: We would like to extend the time of the project. We believe that most of the submitted designs do not comply with our requirements.

Reason: We would like to see a bigger variety of ideas

Target Market(s)

Pretty much to anyone over 20 years old worldwide.

Industry/Entity Type

Nutrition

Requirements
Must have
• It should be attractive, easily recognized, simple yet innovative, durable, functional (easy to use) and easy to store.
Should not have
• Project must not include complex or obnoxious shapes and colours.

```html
<!DOCTYPE html>
<html lang="en">
<head>
<meta charset="utf-8">
<title>Herb Box Dieline</title>
<link rel="stylesheet" href="https://fonts.googleapis.com/css2?family=Cinzel:wght@700&family=Dancing+Script:wght@600&display=swap">
<style>
  :root {
    --backdrop: #ececec;
    --board: #e6eecd;
    --board-mid: #dbe6bd;
    --board-deep: #cfdcaa;
    --cut-line: #6f7568;
    --fold-line: #55594f;
    --label-white: #ffffff;
    --label-stitch: #b9bdb0;
    --herb-green: #4f8a1f;
    --title-green: #3f6a1a;
    --glue-hatch: #7a7f72;
  }
  html, body {
    margin: 0;
    padding: 0;
    width: 1200px;
    height: 1000px;
    overflow: hidden;
    background: var(--backdrop);
  }
  .canvas {
    width: 1200px;
    height: 1000px;
    background: radial-gradient(ellipse at 50% 40%, #f7f7f7 0%, var(--backdrop) 75%);
  }
  .dieline { display: block; width: 1200px; height: 1000px; }
  .board { stroke: var(--cut-line); stroke-width: 1.2; }
  .fold { fill: none; stroke: var(--fold-line); stroke-width: 1; stroke-dasharray: 9 6; }
  .label-window { fill: var(--label-white); }
  .stitch { fill: none; stroke: var(--label-stitch); stroke-width: 1.4; stroke-dasharray: 1.5 3; }
  .glue-hatch { stroke: var(--glue-hatch); stroke-width: 1; }
  .product-type {
    font-family: "Dancing Script", cursive;
    font-weight: 600;
    fill: var(--herb-green);
  }
  .company-name {
    font-family: "Cinzel", serif;
    font-weight: 700;
    fill: var(--title-green);
  }
  .brand-mark { fill: var(--herb-green); }
</style>
</head>
<body>
<div class="canvas">
<svg class="dieline" viewBox="208 55 1368 1140" xmlns="http://www.w3.org/2000/svg">
  <defs>
    <linearGradient id="herbField" gradientUnits="userSpaceOnUse" x1="360" y1="65" x2="1425" y2="1185">
      <stop offset="0" stop-color="var(--board)"/>
      <stop offset="0.18" stop-color="var(--board-mid)"/>
      <stop offset="0.32" stop-color="var(--board)"/>
      <stop offset="0.5" stop-color="var(--board-deep)"/>
      <stop offset="0.66" stop-color="var(--board)"/>
      <stop offset="0.82" stop-color="var(--board-mid)"/>
      <stop offset="1" stop-color="var(--board)"/>
    </linearGradient>
  </defs>

  <g class="carton" role="img" aria-label="Carton board printed with a soft all-over pattern of wild herb sprigs in pale greens">
    <path class="board" fill="url(#herbField)" d="M363 115 V80 Q363 65 378 65 H597 Q612 65 612 80 V115 Z"/>
    <rect class="board" fill="url(#herbField)" x="363" y="115" width="249" height="255"/>
    <path class="board" fill="url(#herbField)" d="M612 370 L622 327 H866 L872 345 L876 370 Z"/>
    <path class="board" fill="url(#herbField)" d="M1122 370 L1130 327 H1376 L1382 345 L1386 370 Z"/>
    <rect class="board" fill="url(#herbField)" x="360" y="370" width="1035" height="510"/>
    <path class="board" fill="url(#herbField)" d="M1395 370 H1425 V920 H1395 Z"/>
    <rect class="board" fill="url(#herbField)" x="360" y="880" width="128" height="40"/>
    <path class="board" fill="url(#herbField)" d="M745 880 H1000 V910 L994 920 H751 L745 910 Z"/>
    <path class="board" fill="url(#herbField)" d="M1255 880 H1395 V920 H1261 L1255 910 Z"/>
    <rect class="board" fill="url(#herbField)" x="488" y="880" width="257" height="260"/>
    <path class="board" fill="url(#herbField)" d="M491 1140 H742 V1170 Q742 1185 727 1185 H506 Q491 1185 491 1170 Z"/>
  </g>

  <g class="glue-hatch">
    <line x1="1398" y1="390" x2="1422" y2="372"/><line x1="1398" y1="440" x2="1422" y2="422"/>
    <line x1="1398" y1="490" x2="1422" y2="472"/><line x1="1398" y1="540" x2="1422" y2="522"/>
    <line x1="1398" y1="590" x2="1422" y2="572"/><line x1="1398" y1="640" x2="1422" y2="622"/>
    <line x1="1398" y1="690" x2="1422" y2="672"/><line x1="1398" y1="740" x2="1422" y2="722"/>
    <line x1="1398" y1="790" x2="1422" y2="772"/><line x1="1398" y1="840" x2="1422" y2="822"/>
    <line x1="1398" y1="890" x2="1422" y2="872"/>
  </g>

  <g class="folds">
    <line class="fold" x1="363" y1="115" x2="612" y2="115"/>
    <line class="fold" x1="360" y1="370" x2="1395" y2="370"/>
    <line class="fold" x1="360" y1="880" x2="1395" y2="880"/>
    <line class="fold" x1="491" y1="1140" x2="742" y2="1140"/>
    <line class="fold" x1="1395" y1="370" x2="1395" y2="920"/>
    <path class="fold" d="M385 375 Q400 620 420 760 L488 880"/>
    <path class="fold" d="M590 375 Q575 620 555 760 L488 880"/>
    <path class="fold" d="M640 375 Q655 620 680 760 L745 880"/>
    <path class="fold" d="M845 375 Q830 620 810 760 L745 880"/>
    <path class="fold" d="M895 375 Q910 620 935 760 L1000 880"/>
    <path class="fold" d="M1100 375 Q1085 620 1065 760 L1000 880"/>
    <path class="fold" d="M1150 375 Q1165 620 1190 760 L1255 880"/>
    <path class="fold" d="M1360 375 Q1345 620 1320 760 L1255 880"/>
  </g>

  <g class="lid-label" transform="rotate(180 489 240)">
    <rect class="label-window" x="383" y="135" width="212" height="210"/>
    <rect class="stitch" x="391" y="143" width="196" height="194"/>
    <circle class="brand-mark" cx="434" cy="190" r="8"/>
    <text class="company-name" x="496" y="196" font-size="18" text-anchor="middle">Herbelia</text>
    <text class="company-name" x="489" y="248" font-size="19" text-anchor="middle">PLACEHOLDER</text>
    <text class="product-type" x="489" y="298" font-size="34" text-anchor="middle">Sage</text>
  </g>

  <g class="details-window">
    <path class="label-window" d="M400 395 H578 Q575 560 545 680 L488 790 L432 680 Q402 560 400 395 Z"/>
    <path class="stitch" d="M409 403 H569 Q566 560 538 676 L488 774 L439 676 Q411 560 409 403 Z"/>
  </g>

  <g class="brand-lockup">
    <circle class="brand-mark" cx="985" cy="530" r="22"/>
    <text class="company-name" x="985" y="610" font-size="32" text-anchor="middle">Herbelia</text>
  </g>

  <g class="type-label">
    <path class="label-window" d="M872 630 Q880 720 955 852 H790 Q865 720 872 630 Z"/>
    <path class="stitch" d="M872 652 Q882 730 944 845 H801 Q862 730 872 652 Z"/>
    <text class="product-type" x="872" y="812" font-size="40" text-anchor="middle">Sage</text>
  </g>
  <g class="type-label">
    <path class="label-window" d="M1128 630 Q1136 720 1211 852 H1046 Q1121 720 1128 630 Z"/>
    <path class="stitch" d="M1128 652 Q1138 730 1200 845 H1057 Q1118 730 1128 652 Z"/>
    <text class="product-type" x="1128" y="812" font-size="40" text-anchor="middle">Sage</text>
  </g>
</svg>
</div>
</body>
</html>
```